Climbing Gear Company Stationary Design

We need some new stationary to standardise our business.
We require:

Business Card
A4 Letterhead
With complements slip

Our business is a Distributor and retailer of rock climbing equipment throughout Australia.
We need to the stationary (business card in particular) to reflect this.

Target Market(s)

customers, other retail outlets, overseas manufacturers.

Industry/Entity Type

Business

Requirements
Must have
• company logo
website url- www.crestwardsupply.com.au
email - marlo@crestwardsupply.com
Business Address: Unit 3, 14-16 Quarry Close, Bellingrove, NSW, 2461
Phone: 0491 637 208
my Name (on Business card) - Marlon Pettigrew
use of Blue colour in our logo

```html
<!DOCTYPE html>
<html lang="en">
<head>
<meta charset="utf-8">
<title>Crestward Supply – Business Card</title>
<link rel="stylesheet" href="https://fonts.googleapis.com/css2?family=Michroma&family=Open+Sans:wght@400;600&display=swap">
<style>
  :root {
    --brand-blue: #2b4c9f;
    --brand-blue-light: #3559b0;
    --brand-blue-deep: #1f3a86;
    --card-white: #ffffff;
    --ink: #1c1c1c;
    --backdrop: #e6e9ec;
  }
  * { box-sizing: border-box; margin: 0; padding: 0; }
  html, body { width: 1200px; height: 960px; overflow: hidden; }
  body {
    background: var(--backdrop);
    font-family: "Open Sans", Arial, sans-serif;
    display: flex;
    flex-direction: column;
    align-items: center;
    justify-content: center;
    gap: 48px;
  }
  .card {
    position: relative;
    width: 680px;
    height: 416px;
    overflow: hidden;
    box-shadow: 0 6px 18px rgba(0,0,0,0.18);
  }

  /* Front */
  .card-front {
    background: linear-gradient(135deg, var(--brand-blue-light), var(--brand-blue));
    color: var(--card-white);
  }
  .card-front .wave { position: absolute; left: 0; bottom: 0; width: 100%; height: 200px; }
  .front-brand {
    position: absolute;
    top: 120px;
    left: 0; right: 0;
    text-align: center;
  }
  .wordmark {
    font-family: "Michroma", Arial, sans-serif;
    font-size: 38px;
    letter-spacing: 1px;
    color: var(--card-white);
    white-space: nowrap;
  }
  .tagline {
    margin-top: 14px;
    font-size: 21px;
    letter-spacing: 3px;
    color: var(--card-white);
    white-space: nowrap;
  }

  /* Back */
  .card-back { background: var(--card-white); color: var(--ink); }
  .name-tab {
    position: absolute;
    top: 52px;
    left: 0;
    width: 440px;
    height: 58px;
    background: var(--brand-blue);
    border-radius: 0 12px 12px 0;
    display: flex;
    align-items: center;
    padding-left: 70px;
    font-family: "Michroma", Arial, sans-serif;
    font-size: 22px;
    color: var(--card-white);
    letter-spacing: 0.5px;
    white-space: nowrap;
  }
  .contact-list {
    position: absolute;
    top: 142px;
    left: 38px;
    list-style: none;
    font-size: 19px;
    line-height: 26px;
  }
  .contact-list li { display: flex; align-items: center; gap: 20px; }
  .contact-list svg { width: 14px; height: 14px; fill: var(--brand-blue); flex: none; }
  .address {
    position: absolute;
    top: 262px;
    left: 38px;
    font-size: 19px;
    line-height: 24px;
    font-style: normal;
  }
  .back-brand {
    position: absolute;
    right: 34px;
    bottom: 52px;
    font-family: "Michroma", Arial, sans-serif;
    font-size: 17px;
    color: var(--brand-blue);
    letter-spacing: 0.5px;
    white-space: nowrap;
  }
</style>
</head>
<body>

  <section class="card card-front" aria-label="Business card front">
    <svg class="wave" viewBox="0 0 680 200" preserveAspectRatio="none" aria-hidden="true">
      <path d="M0 90 C 180 150, 420 150, 680 40 L680 200 L0 200 Z" fill="var(--brand-blue-deep)"/>
      <path d="M0 70 C 200 140, 430 140, 680 30 L680 44 C 430 160, 200 160, 0 96 Z" fill="var(--card-white)"/>
      <path d="M0 110 C 200 170, 440 170, 680 60 L680 200 L0 200 Z" fill="var(--brand-blue-deep)" opacity="0.55"/>
    </svg>
    <div class="front-brand">
      <div class="wordmark">CRESTWARD SUPPLY</div>
      <div class="tagline">THE KIT • THE CLIMB • THE OUTDOORS</div>
    </div>
  </section>

  <section class="card card-back" aria-label="Business card back">
    <div class="name-tab">Marlon Pettigrew</div>
    <ul class="contact-list">
      <li>
        <svg viewBox="0 0 16 16" aria-hidden="true"><path d="M3 1h3l1.5 4-2 1.3a9 9 0 0 0 4.2 4.2L11 8.5l4 1.5v3a2 2 0 0 1-2 2A13 13 0 0 1 1 3a2 2 0 0 1 2-2z"/></svg>
        <span>0491 637 208</span>
      </li>
      <li>
        <svg viewBox="0 0 16 16" aria-hidden="true"><path d="M1 3h14v10H1z M1 3l7 6 7-6" stroke="var(--card-white)" stroke-width="1.2"/></svg>
        <span>marlo@crestwardsupply.com</span>
      </li>
      <li>
        <svg viewBox="0 0 16 16" aria-hidden="true"><circle cx="8" cy="8" r="7"/><path d="M1 8h14M8 1c3 3 3 11 0 14M8 1c-3 3-3 11 0 14" stroke="var(--card-white)" stroke-width="1" fill="none"/></svg>
        <span>www.crestwardsupply.com.au</span>
      </li>
    </ul>
    <address class="address">
      Unit 3, 14-16 Quarry Close,<br>
      Bellingrove, NSW, 2461
    </address>
    <div class="back-brand">CRESTWARD SUPPLY</div>
  </section>

</body>
</html>
```